Blue Heron Courier & Delivery Services needs a flyer

We need an introductory flyer for a new company based in Yellowknife, Northwest Territories,Canada. Our company name is Blue Heron Courier & Delivery Services. We will be handling envelopes and small packages up to 20 pounds. We expect 20 percent of our business to come from residential customers and 80 percent from the business community including lawyers, doctors, engineers and government offices. The main message that we will try to convey in this flyer is that we are a new and exciting company that promises to make 100% customer satisfaction our number one goal. I would like the layout to be elegant and simple and certainly not cluttered. It will be a single sided flyer. Text should be easy to read and most likely at most two fonts. I would like one stunning image or photo relating to the courier business and message. There should be plenty of white space throughout the flyer and nice margins on all sides. I would like my flyer to be 8.5 inches by 11 inches and it should read from top to bottom. . I would like a nice big bold headline that in some way mentions " Special Offer- Up to 100% Off. You can change the wording if you have a better idea. Throughout the flyer you can highlight and italicize for emphasis. Please try to use bullet points for my five main reasons for hiring our company which are: you will be 100% satisfied with each delivery or you will be given a complete refund no questions asked, your envelope or package will be delivered on time every time, you will always be treated throughout the delivery process in a professional manner, you will be given the widest selection in Yellowknife of price points and delivery options , you can trust us with your most important and time sensitive deliveries. Try to incorporate something next to these five points to really draw attention like a check mark, star etc.... I would prefer if my company name and contact info is in the bottom third of the flyer. My email is blueheroncourieryk@mailbox-example.net. My phone number is 867-312-7794. It might be a good idea to have my phone number also at the top of the flyer someplace after the headline saying like Call Now!!! you can use boxes, borders and contrasting bold colors to bring flyer to life. I have a testimonial from a business owner that I dealt with when I ran another business which would be nice to have included . " While receiving daily deliveries for 18 years from Calvin Marsh I found him to be punctual , reliable and efficient " Glen Potter, owner of Potter and Lindqvist Trading LTD, Yellowknife,NWT. I thought perhaps at the top of flyer after the headline perhaps in some way you could say Yellowknife's newest and best courier and delivery service is pleased to offer the following stunning discounts: then you could list the three special offers: 1) First 5 businesses to book regular scheduled deliveries will get 100% off their first delivery. 2) First 5 businesses to book a single delivery will get 50% off that delivery. 3) First 5 residential customers to book a delivery will receive 25% off that delivery. I thought you could mention my name somewhere. Calvin Marsh. Owner has lived in Yellowknife for 42 years and has 20 years experience doing performing important and time sensitive deliveries. Perhaps you could mention somewhere that we will have a couple of ongoing discounts also which will be 1) seniors discounts. 2) regular scheduled deliveries discounts. I have suggested colors but if you have other ideas I would certainly look at them. Our business tag line is. On Time Every Time
Target Market(s)
Business owners typically males 30-50 years old
Industry/Entity Type
Delivery Service
Requirements
Must have
- Done in CMYK mode sufficient bleed size for printing
Nice to have
- Nothing set in stone. I recently had my logo design uploaded to this brief. It is up to you if you feel it should be included in the flyer.
Should not have
- I am willing to look at any design

```html
<!DOCTYPE html>
<html lang="en">
<head>
<meta charset="utf-8">
<title>Blue Heron Courier &amp; Delivery Services – Flyer</title>
<link rel="stylesheet" href="https://fonts.googleapis.com/css2?family=Open+Sans:ital,wght@0,400;0,600;0,700;0,800;1,400;1,600;1,700;1,800&display=swap">
<style>
  :root {
    --red: #e5232d;
    --navy: #132a4a;
    --blue: #2a73b6;
    --blue-light: #3a7dbf;
    --ink: #1b1b1b;
    --white: #ffffff;
    --pale: #f6f8fb;
  }
  * { box-sizing: border-box; margin: 0; padding: 0; }
  html, body { width: 927px; height: 1200px; overflow: hidden; background: var(--white); }
  body { font-family: "Open Sans", Arial, sans-serif; color: var(--ink); }
  .flyer { position: relative; width: 927px; height: 1200px; overflow: hidden; background: var(--white); }

  .offer-band { position: absolute; left: 0; top: 0; width: 927px; height: 121px; background: var(--red); }
  .offer-upto { position: absolute; left: 30px; top: 4px; color: var(--white); font-weight: 700; font-style: italic; font-size: 31px; }
  .offer-pct { position: absolute; left: 52px; top: 26px; color: var(--white); font-weight: 800; font-style: italic; font-size: 88px; line-height: 1; letter-spacing: -2px; }
  .offer-off { position: absolute; left: 296px; top: 40px; color: var(--white); font-weight: 700; font-style: italic; font-size: 26px; }
  .offer-title { position: absolute; left: 360px; top: 14px; color: var(--white); font-weight: 800; font-style: italic; font-size: 41px; line-height: 1.1; white-space: nowrap; }
  .offer-call { position: absolute; left: 360px; top: 66px; color: var(--navy); font-weight: 700; font-size: 19px; white-space: nowrap; }
  .offer-call strong { font-size: 44px; font-weight: 600; margin-left: 2px; vertical-align: -6px; letter-spacing: -0.5px; }

  .courier-photo { position: absolute; left: 768px; top: 0; width: 159px; height: 278px;
    background: linear-gradient(160deg, #e9d8c4 0%, #c9a57f 45%, #9c7651 100%); }

  .headline { position: absolute; left: 30px; top: 133px; color: var(--blue); font-weight: 800; font-size: 62px; line-height: 1.05; letter-spacing: -0.5px; }

  .discount-band { position: absolute; left: 0; top: 280px; width: 927px; height: 318px; background: var(--blue); color: var(--white); }
  .discount-intro { position: absolute; left: 42px; top: 14px; font-weight: 700; font-style: italic; font-size: 26.5px; line-height: 1.38; }
  .discount-list { position: absolute; left: 92px; top: 100px; list-style: none; }
  .discount-list li { position: relative; padding-left: 42px; font-style: italic; font-size: 25px; line-height: 1.27; margin-bottom: 3px; }
  .discount-list svg { position: absolute; left: 0; top: 6px; width: 26px; height: 26px; }

  .reasons { position: absolute; left: 0; top: 598px; width: 927px; height: 463px; background: var(--pale); }
  .truck-icon { position: absolute; left: 52px; top: 80px; width: 84px; height: 70px; }
  .why-badge { position: absolute; left: 104px; top: 100px; width: 150px; height: 150px; border-radius: 50%; background: var(--blue); color: var(--white);
    display: flex; align-items: center; justify-content: center; text-align: center; font-style: italic; font-size: 36px; line-height: 1.05; }
  .reason-list { position: absolute; left: 288px; top: 22px; width: 620px; list-style: none; }
  .reason-list li { position: relative; padding-left: 38px; font-style: italic; font-size: 21px; line-height: 1.35; margin-bottom: 4px; }
  .reason-list svg { position: absolute; left: 0; top: 4px; width: 22px; height: 22px; }

  .testimonial { position: absolute; left: 52px; top: 330px; width: 850px; }
  .testimonial-quote { font-weight: 700; font-style: italic; font-size: 25.5px; line-height: 1.3; }
  .testimonial-name { margin-top: 8px; font-weight: 700; font-size: 19px; }
  .testimonial-role { font-style: italic; font-size: 16px; }

  .contact-band { position: absolute; left: 0; top: 1061px; width: 927px; height: 139px; background: var(--blue-light); color: var(--white); }
  .owner-bio { position: absolute; left: 34px; top: 22px; width: 450px; font-style: italic; font-size: 17px; line-height: 1.6; }
  .owner-bio strong { font-style: normal; font-weight: 600; }
  .contact-list { position: absolute; left: 505px; top: 35px; list-style: none; }
  .contact-list li { display: flex; align-items: center; gap: 14px; font-size: 17px; margin-bottom: 18px; white-space: nowrap; }
  .contact-list svg { width: 26px; height: 22px; flex: none; }
</style>
</head>
<body>
<main class="flyer">
  <header class="offer-band">
    <span class="offer-upto">Up to</span>
    <span class="offer-pct">100%</span>
    <span class="offer-off">Off</span>
    <span class="offer-title">Stunning Discounts</span>
    <span class="offer-call">Call now: <strong>867-312-7794</strong></span>
  </header>

  <div class="courier-photo" role="img" aria-label="Photo of a smiling courier carrying a stack of cardboard parcels"></div>

  <h1 class="headline">Blue Heron Courier<br>&amp; Delivery Services</h1>

  <section class="discount-band">
    <p class="discount-intro">Yellowknife’s newest and best city courier and delivery<br>service is pleased to offer the following stunning discounts:</p>
    <ul class="discount-list">
      <li><svg viewBox="0 0 26 26"><rect x="2" y="5" width="19" height="19" fill="none" stroke="#fff" stroke-width="2.4"/><path d="M6 14l5 5L24 3" fill="none" stroke="#fff" stroke-width="3"/></svg>First 5 businesses to book regular scheduled deliveries<br>will get 100% off their first delivery.</li>
      <li><svg viewBox="0 0 26 26"><rect x="2" y="5" width="19" height="19" fill="none" stroke="#fff" stroke-width="2.4"/><path d="M6 14l5 5L24 3" fill="none" stroke="#fff" stroke-width="3"/></svg>First 5 businesses to book a single delivery<br>will get 50% off that delivery.</li>
      <li><svg viewBox="0 0 26 26"><rect x="2" y="5" width="19" height="19" fill="none" stroke="#fff" stroke-width="2.4"/><path d="M6 14l5 5L24 3" fill="none" stroke="#fff" stroke-width="3"/></svg>First 5 residential customers to book a delivery<br>will receive 25% off that delivery.</li>
    </ul>
  </section>

  <section class="reasons">
    <svg class="truck-icon" viewBox="0 0 84 70" aria-hidden="true">
      <rect x="2" y="8" width="50" height="40" rx="4" fill="#2a73b6"/>
      <path d="M56 20h14l12 14v14H56z" fill="#2a73b6"/>
      <circle cx="18" cy="56" r="9" fill="#2a73b6" stroke="#f6f8fb" stroke-width="3"/>
      <circle cx="68" cy="56" r="9" fill="#2a73b6" stroke="#f6f8fb" stroke-width="3"/>
    </svg>
    <div class="why-badge">Why<br>us??</div>
    <ul class="reason-list">
      <li><svg viewBox="0 0 22 22"><rect x="1.5" y="4" width="16" height="16" fill="none" stroke="#2a73b6" stroke-width="2"/><path d="M5 12l4 4L20 2" fill="none" stroke="#2a73b6" stroke-width="2.6"/></svg>100% satisfaction with each delivery or you will<br>be given a complete refund no questions asked,</li>
      <li><svg viewBox="0 0 22 22"><rect x="1.5" y="4" width="16" height="16" fill="none" stroke="#2a73b6" stroke-width="2"/><path d="M5 12l4 4L20 2" fill="none" stroke="#2a73b6" stroke-width="2.6"/></svg>On time delivery! Every time.</li>
      <li><svg viewBox="0 0 22 22"><rect x="1.5" y="4" width="16" height="16" fill="none" stroke="#2a73b6" stroke-width="2"/><path d="M5 12l4 4L20 2" fill="none" stroke="#2a73b6" stroke-width="2.6"/></svg>You will always be treated throughout the delivery<br>process in a professional manner,</li>
      <li><svg viewBox="0 0 22 22"><rect x="1.5" y="4" width="16" height="16" fill="none" stroke="#2a73b6" stroke-width="2"/><path d="M5 12l4 4L20 2" fill="none" stroke="#2a73b6" stroke-width="2.6"/></svg>You will be given the widest selection in Yellowknife<br>of price points and delivery options ,</li>
      <li><svg viewBox="0 0 22 22"><rect x="1.5" y="4" width="16" height="16" fill="none" stroke="#2a73b6" stroke-width="2"/><path d="M5 12l4 4L20 2" fill="none" stroke="#2a73b6" stroke-width="2.6"/></svg>You can trust us with your most important and<br>time sensitive deliveries.</li>
    </ul>

    <blockquote class="testimonial">
      <p class="testimonial-quote">“ While receiving daily deliveries for 18 years from Calvin Marsh<br>I found him to be punctual, reliable and efficient ”</p>
      <p class="testimonial-name">Glen Potter</p>
      <p class="testimonial-role">Owner: Potter and Lindqvist Trading LTD, Yellowknife, NWT</p>
    </blockquote>
  </section>

  <footer class="contact-band">
    <p class="owner-bio"><strong>Calvin Marsh.</strong> Owner has lived in Yellowknife for 42 years and has 20 years experience performing important and time sensitive deliveries.</p>
    <ul class="contact-list">
      <li><svg viewBox="0 0 26 22" aria-hidden="true"><rect x="2" y="3" width="20" height="15" fill="none" stroke="#fff" stroke-width="2"/><path d="M2 3l10 8 10-8" fill="none" stroke="#fff" stroke-width="2"/></svg>blueheroncourieryk@mailbox-example.net</li>
      <li><svg viewBox="0 0 26 22" aria-hidden="true"><path d="M2 8c0-4 22-4 22 0v2h-6V7H8v3H2z" fill="#fff"/><rect x="5" y="11" width="16" height="9" rx="2" fill="#fff"/></svg>867-312-7794</li>
    </ul>
  </footer>
</main>
</body>
</html>
```